KESTRELMAR NAUTICA SUPPLIERS SELL SHEETS

Create a group of Sell Sheets that can be used in client meetings and willbe incorporated into web site pages in the future. We wish to highlight our Mission Statement / Company Bio / Services and Products offered. This piece may be 8 to 12 pages. In the near future this will grow to include an on-line Catalog with 300 to 500 pages of product offerings.

It will not list individual products and prices but rather will serve as a New Business introduction using brief descriptive text and a lot of industry photos. At this time we do have a Logo and Tag Line which will be used.

The image we need to portray is High End Quality Sales, Service, Professional Industry Experience and Reliability. My personal experience includes 27 years as a ship´s Captain working all over the world.

We are a start-up Ship´s Chandler service, located in Porto Serenil, Brasil. We will sell products and inspection services to the Offshore Petroleum Industry which includes vessels and platforms. These products will include the simple monthly supply replenishment (like paper towels / laundry soap / drinking water) to the more technical, like Pop Off Valves (sales & inspection certifications), Transfer Hoses, Sales Service and Certifications, OEM Filters for Engines& Generators, Anchor Harware, Nautical Bulbs & Light Fixtures Safety Gear and hundreds of other items.

We will have a group of EMERGENCY GEAR on-hand in our warehouse, to supply in cases like a lost anchor for example. We willoffer a Guaranteed 30 hour delivery anywhere in Brasil. These vessels work at a rate of up to $50K per day and cannot afford what is called`Down Time` or time off the clock.

All text will be supplied in both English and Portuguese. I prefer that each block of text will show both languages with a distinctive color or typeface for each. Please present your ideas on how to deal with the two languages.

Sorry for any mis-spellings but today I am forced to work on a Portuguese keyboard.

Target Market(s)

Ship´s Captains, Purchasing Managers, Company Directors, Engineers

Industry/Entity Type

Business

Requirements
Must have
• I am open to a Professional, High End look. I would like to incorporate photos and ``historical`` illustrations to tella story, which I will supply.

I have attached our new Company Logo which has the tag line....``TO STAY THE COURSE´´. We would like to repeat the logo and tag line whenever possible without being too obnoxious.

```html
<!DOCTYPE html>
<html lang="en">
<head>
<meta charset="utf-8">
<title>Kestrelmar Nautica Suppliers – Sell Sheet</title>
<link rel="stylesheet" href="https://fonts.googleapis.com/css2?family=Open+Sans:wght@400;600;700;800&family=Tinos:wght@400;700&display=swap">
<style>
  :root {
    --green: #2f5a17;
    --green-dark: #234511;
    --gold: #f2b51c;
    --gold-soft: #f6c94a;
    --brown: #6b3d1b;
    --paper: #ffffff;
    --ink: #1d1d1d;
    --rule: #3a3a3a;
    --backdrop: #ece8df;
  }
  * { box-sizing: border-box; margin: 0; padding: 0; }
  html, body { width: 1200px; height: 960px; overflow: hidden; }
  body {
    background: var(--backdrop);
    position: relative;
    font-family: "Open Sans", Arial, sans-serif;
    color: var(--ink);
  }

  /* ---------- sheets ---------- */
  .sheet {
    position: absolute;
    background: var(--paper);
    overflow: hidden;
    box-shadow: 0 2px 10px rgba(0,0,0,.25);
  }
  .sheet-front { left: 360px; top: 20px; width: 820px; height: 520px; }
  .sheet-inner { left: 14px; top: 556px; width: 620px; height: 390px; }

  .fold { position: absolute; top: 0; bottom: 0; width: 1px; background: var(--rule); }

  .shape { position: absolute; inset: 0; width: 100%; height: 100%; }

  .sheet-caption {
    position: absolute;
    font-family: "Open Sans", Arial, sans-serif;
    font-weight: 700;
    font-size: 20px;
    color: #1a1a1a;
  }
  .caption-front { left: 1030px; top: 556px; }
  .caption-inner { left: 650px; top: 906px; }

  /* ---------- front side ---------- */
  .compass-art { position: absolute; left: 40px; top: 150px; width: 400px; height: 400px; }

  .tagline {
    position: absolute;
    left: 370px; top: 205px;
    transform: rotate(-35deg);
    transform-origin: left bottom;
    white-space: nowrap;
  }
  .tagline-text {
    font-weight: 800;
    font-size: 31px;
    letter-spacing: .5px;
    color: var(--green);
    line-height: 1;
  }
  .tagline-bar {
    height: 6px;
    margin-top: 3px;
    margin-left: -14px;
    width: 320px;
    background: linear-gradient(90deg, var(--gold), var(--brown));
  }

  .brand-mark {
    position: absolute;
    left: 290px; top: 46px; width: 240px;
    display: flex; align-items: center; gap: 10px;
  }
  .brand-dot {
    flex: 0 0 auto;
    width: 44px; height: 44px; border-radius: 50%;
    background: var(--gold);
  }
  .brand-name {
    font-weight: 800; font-size: 17px; line-height: 1.1;
    color: var(--green);
  }

  .cover-title {
    position: absolute;
    left: 565px; top: 328px;
    font-weight: 700;
    line-height: 1;
  }
  .cover-title .t-gold { color: var(--gold); font-size: 19px; }
  .cover-title .t-green { color: var(--green); font-size: 27px; }
  .cover-title .line2 { display: block; color: var(--gold); font-size: 19px; margin-top: 3px; }

  /* ---------- inner side ---------- */
  .lang-tab {
    position: absolute; left: 6px; top: 4px;
    font-weight: 700; font-size: 14px; color: #fff;
  }
  .col { position: absolute; top: 0; bottom: 0; }
  .col-english { left: 8px; width: 192px; top: 34px; }
  .col-photos { left: 207px; width: 206px; }
  .col-portuguese { left: 420px; width: 190px; top: 40px; }

  .pill {
    display: inline-block;
    background: var(--gold-soft);
    border-radius: 50%/50%;
    padding: 1px 14px;
    font-weight: 700; font-size: 10px;
    color: var(--ink);
    margin: 0 0 4px 10px;
  }
  .body-copy {
    font-family: "Tinos", "Times New Roman", serif;
    font-size: 6.6px;
    line-height: 1.3;
    margin-bottom: 7px;
  }
  .bullets { list-style: none; }
  .bullets li {
    position: relative; padding-left: 10px;
    font-size: 7.4px; line-height: 1.25; margin-bottom: 2px;
  }
  .bullets li::before {
    content: ""; position: absolute; left: 0; top: 2px;
    width: 6px; height: 6px; border-radius: 50%; background: var(--green);
  }
  .bullets-en li { font-weight: 700; font-size: 7.8px; }
  .bullets-pt li { font-size: 6.6px; }

  .photo { position: absolute; }
  .photo-plant  { left: 0;   top: 30px;  width: 100px; height: 60px;
                  background: linear-gradient(135deg, #8aa2b8, #41576c); }
  .photo-shop   { left: 96px; top: 100px; width: 100px; height: 64px;
                  background: linear-gradient(135deg, #c98a3a, #5d6a73); }
  .photo-yacht  { left: 0;   top: 168px; width: 100px; height: 72px;
                  background: linear-gradient(180deg, #c9d6e2, #6b8aa8 60%, #3d5a78); }
  .photo-gears  { left: 96px; top: 246px; width: 100px; height: 72px;
                  background: linear-gradient(135deg, #5a5f63, #1f2326); }
  .photo-rig    { left: 0;   top: 326px; width: 146px; height: 56px;
                  background: linear-gradient(180deg, #b9d3ea, #4d7fae 65%, #2c557e); }
</style>
</head>
<body>

  <!-- Front side -->
  <section class="sheet sheet-front" aria-label="Front side">
    <svg class="shape" viewBox="0 0 820 520" preserveAspectRatio="none" aria-hidden="true">
      <defs>
        <linearGradient id="front-top" x1="0" x2="1" y1="0" y2="0">
          <stop offset="0" stop-color="#2f5a17"/>
          <stop offset=".45" stop-color="#6f7a1c"/>
          <stop offset="1" stop-color="#f2b51c"/>
        </linearGradient>
        <linearGradient id="front-bottom" x1="1" x2="0" y1="0" y2="1">
          <stop offset="0" stop-color="#f2b51c"/>
          <stop offset=".55" stop-color="#d3a51c"/>
          <stop offset="1" stop-color="#2f5a17"/>
        </linearGradient>
      </defs>
      <path d="M0,0 H480 C300,8 110,50 0,175 Z" fill="url(#front-top)"/>
      <path d="M820,250 C790,410 640,500 430,520 H820 Z" fill="url(#front-bottom)"/>
    </svg>

    <div class="fold" style="left:273px"></div>
    <div class="fold" style="left:547px"></div>

    <svg class="compass-art" viewBox="0 0 400 400" role="img" aria-label="Illustration of a gold compass rose on a sketched round log slice">
      <defs>
        <radialGradient id="compass-fill" cx=".5" cy=".5" r=".5">
          <stop offset="0" stop-color="#e6b43a"/>
          <stop offset=".55" stop-color="#efe6d4"/>
          <stop offset=".92" stop-color="#d9c7a6"/>
          <stop offset="1" stop-color="#6b3d1b"/>
        </radialGradient>
      </defs>
      <circle cx="200" cy="200" r="195" fill="url(#compass-fill)"/>
    </svg>

    <div class="tagline">
      <div class="tagline-text">TO STAY THE COURSE</div>
      <div class="tagline-bar"></div>
    </div>

    <div class="brand-mark">
      <span class="brand-dot"></span>
      <span class="brand-name">KESTRELMAR NAUTICA SUPPLIERS</span>
    </div>

    <h1 class="cover-title">
      <span class="t-gold">KESTRELMAR</span> <span class="t-green">NAUTICA</span>
      <span class="line2">SUPPLIERS</span>
    </h1>
  </section>
  <div class="sheet-caption caption-front">Front side</div>

  <!-- Inner side -->
  <section class="sheet sheet-inner" aria-label="Inner side">
    <svg class="shape" viewBox="0 0 620 390" preserveAspectRatio="none" aria-hidden="true">
      <defs>
        <linearGradient id="inner-top" x1="0" x2="1">
          <stop offset="0" stop-color="#2f5a17"/>
          <stop offset=".3" stop-color="#5c6d1a"/>
          <stop offset="1" stop-color="#f2b51c"/>
        </linearGradient>
        <linearGradient id="inner-bottom" x1="0" x2="1">
          <stop offset="0" stop-color="#f2b51c"/>
          <stop offset=".6" stop-color="#b89a1d"/>
          <stop offset="1" stop-color="#2f5a17"/>
        </linearGradient>
      </defs>
      <path d="M0,0 H420 C260,4 150,12 80,26 H0 Z" fill="url(#inner-top)"/>
      <path d="M0,372 C200,378 420,372 530,352 C580,340 605,320 620,290 V390 H0 Z" fill="url(#inner-bottom)"/>
    </svg>

    <div class="lang-tab">ENGLISH</div>

    <div class="fold" style="left:207px; bottom:16px"></div>
    <div class="fold" style="left:413px; bottom:20px"></div>

    <div class="col col-english" lang="en">
      <h2 class="pill">INTRODUCTION</h2>
      <p class="body-copy">We are a start-up Ship´s Chandler service, located in Porto Serenil, Brasil. We will sell products and inspection services to the Offshore Petroleum Industry which includes vessels and platforms. These products will include the simple monthly supply replenishment (like paper towels / laundry soap / drinking water) to the more technical, like Pop Off Valves (sales &amp; inspection certifications), Transfer Hoses, Sales Service and Certifications, OEM Filters for Engines&amp; Generators, Anchor Harware, Nautical Bulbs &amp; Light Fixtures Safety Gear and hundreds of other items.</p>
      <p class="body-copy">We will have a group of EMERGENCY GEAR on-hand in our warehouse, to supply in cases like a lost anchor for example. We willoffer a Guaranteed 30 hour delivery anywhere in Brasil. These vessels work at a rate of up to $50K per day and cannot afford what is called`Down Time` or time off the clock.</p>
      <h2 class="pill">SERVICES</h2>
      <ul class="bullets bullets-en">
        <li>Services to the Offshore Petroleum Industry which includes vessels.</li>
        <li>Transfer Hoses, Sales Service and Certifications.</li>
        <li>EMERGENCY GEAR group.</li>
        <li>OEM Filters for Engines&amp; Generators, Anchor Harware, Nautical Bulbs.</li>
      </ul>
    </div>

    <div class="col col-photos">
      <div class="photo photo-plant" role="img" aria-label="Photo of engineers at work in an industrial plant"></div>
      <div class="photo photo-shop" role="img" aria-label="Photo of a workshop hall with machinery"></div>
      <div class="photo photo-yacht" role="img" aria-label="Photo of a large white vessel at sea"></div>
      <div class="photo photo-gears" role="img" aria-label="Photo of heavy steel gears and engine parts"></div>
      <div class="photo photo-rig" role="img" aria-label="Photo of an offshore petroleum platform"></div>
    </div>

    <div class="col col-portuguese" lang="pt">
      <p class="body-copy">Somos um serviço de Ship Chandler em fase inicial, localizado em Porto Serenil, Brasil. Venderemos produtos e serviços de inspeção para a Indústria Offshore de Petróleo, que inclui embarcações e plataformas. Estes produtos incluem a reposição mensal simples (como papel toalha / sabão / água potável) até os mais técnicos, como Válvula de alívio (vendas e certificações de inspeção), mangueiras de transferência, vendas, serviços e certificações, Filtros de OEM para Motores e Geradores, âncora Harware, lâmpadas náuticas e equipamentos de segurança luminárias e centenas de outros itens.</p>
      <p class="body-copy">Nós temos um grupo de equipamentos de emergência na mão em nosso armazém, para suprir, em casos como uma âncora perdida por exemplo. Nós willoffer uma entrega garantida 30 horas em qualquer lugar no Brasil. Estas embarcações trabalhar em uma taxa de até R $ 50 mil por dia e não pode pagar o que é chamado `Down Time`ou tempo fora do relógio.</p>
      <h2 class="pill">SERVIÇOS</h2>
      <ul class="bullets bullets-pt">
        <li>Serviços para o Petróleo Offshore Indústria, que inclui vasos.</li>
        <li>Mangueiras de transferência, o serviço de vendas Certificações.</li>
        <li>Grupo de equipamentos de emergência.</li>
        <li>Filtros de OEM para Motores e Geradores, Hardware âncora, lâmpadas náuticas.</li>
      </ul>
    </div>
  </section>
  <div class="sheet-caption caption-inner">Inner side</div>

</body>
</html>
```